Fun relaxed Travel Photography Business Card*

Require a fun, funky and quirky but rememberable business card for a travel photographer

Industry/Entity Type

Photographer

Contact Information for Business Card

Front Card

(my name) Tavo M.

Travel Photographer ( small under travel photographer) “self-proclaimed”

(website logo) wanderingtavo.example

(Instagram logo) @wandering_with_tavo

(Instagram logo) @wandering_with_tavo_2.0 (backup for when Instagram puts Tavo on timeout for bad behaviour)

Tel: N/A (removing the potential awkwardness of me not replying)

Email: (see above)

Back Card

Offending people since 1986

(Bottom right corner) “p.s. travelling made me fatTER”

Font styles to use
Serif

Colors

Designer to choose colors to be used in the design.

Requirements
Must have
• a camera
• a similar cartoon version of me as the "logo" see attached files, try to make as similar as possible

```html
<!DOCTYPE html>
<html lang="en">
<head>
<meta charset="utf-8">
<title>Tavo M. — Travel Photographer Business Card</title>
<link rel="stylesheet" href="https://fonts.googleapis.com/css2?family=Questrial&family=Montserrat:ital,wght@0,500;0,700;1,400&family=Oswald:wght@500&family=Pinyon+Script&display=swap">
<style>
  :root {
    --stage: #353036;
    --card-night: #14151c;
    --card-dusk: #2a3140;
    --glow: #c7683a;
    --ink-white: #f4f2f5;
    --magenta: #e64fe0;
    --violet: #7a3bd9;
    --coral: #f0716a;
    --sky: #2f7df0;
    --mint: #5ed6c0;
    --silver: #cfd3d8;
  }
  * { margin: 0; padding: 0; box-sizing: border-box; }
  html, body {
    width: 911px; height: 1200px; overflow: hidden;
    background: var(--stage);
  }
  .card {
    position: absolute; left: 74px; width: 766px; height: 437px;
    border-radius: 13px; overflow: hidden;
    box-shadow: 0 6px 18px rgba(0,0,0,.45);
  }
  .card--front { top: 57px; }
  .card--back { top: 554px; }
  .card__art { position: absolute; inset: 0; width: 100%; height: 100%; }

  .identity { position: absolute; left: 516px; top: 176px; }
  .identity__name {
    font-family: "Montserrat", sans-serif; font-weight: 700;
    font-size: 25px; letter-spacing: 9px; color: var(--ink-white);
    line-height: 1;
  }
  .identity__role {
    margin-top: 9px;
    font-family: "Questrial", sans-serif; font-size: 21px;
    color: var(--magenta); line-height: 1.1;
  }
  .identity__note {
    margin-top: 2px;
    font-family: "Montserrat", sans-serif; font-style: italic; font-weight: 400;
    font-size: 18px; color: var(--ink-white); line-height: 1.2;
  }
  .identity__site {
    position: absolute; left: 511px; top: 263px;
    font-family: "Questrial", sans-serif; font-size: 20.5px;
    color: var(--magenta); letter-spacing: .3px;
  }
  .social { position: absolute; left: 471px; top: 389px; display: flex; align-items: center; gap: 5px; }
  .social__mark {
    width: 34px; height: 34px; border: 3px solid var(--magenta); border-radius: 9px;
  }
  .social__handles {
    font-family: "Questrial", sans-serif; font-size: 13.5px;
    color: var(--magenta); line-height: 1.35;
  }

  .motto {
    position: absolute; left: 0; right: 0; top: 364px; text-align: center;
    font-family: "Oswald", sans-serif; font-weight: 500; font-size: 22px;
    letter-spacing: 11px; color: var(--ink-white); line-height: 1;
  }
  .postscript {
    position: absolute; left: 0; right: 0; top: 398px; text-align: center;
    font-family: "Pinyon Script", serif; font-size: 26px;
    color: var(--ink-white); line-height: 1;
  }
</style>
</head>
<body>

<section class="card card--front">
  <svg class="card__art" viewBox="0 0 766 437" xmlns="http://www.w3.org/2000/svg">
    <defs>
      <radialGradient id="frontGlow" cx="0.45" cy="0.3" r="0.5">
        <stop offset="0" stop-color="#6b4a36"/>
        <stop offset="1" stop-color="#17181f" stop-opacity="0"/>
      </radialGradient>
      <linearGradient id="frontNight" x1="0" y1="0" x2="0" y2="1">
        <stop offset="0" stop-color="#1c1f28"/>
        <stop offset="0.55" stop-color="#3a2a26"/>
        <stop offset="1" stop-color="#111217"/>
      </linearGradient>
      <linearGradient id="ringMagenta" x1="0" y1="0" x2="0.4" y2="1">
        <stop offset="0" stop-color="#d94fe6"/>
        <stop offset="0.55" stop-color="#6a35d8"/>
        <stop offset="1" stop-color="#f0716a"/>
      </linearGradient>
      <linearGradient id="arcViolet" x1="0" y1="0" x2="0" y2="1">
        <stop offset="0" stop-color="#8b3de0"/>
        <stop offset="0.5" stop-color="#3b5ae8"/>
        <stop offset="1" stop-color="#f0716a"/>
      </linearGradient>
      <linearGradient id="arcSky" x1="0" y1="0" x2="0" y2="1">
        <stop offset="0" stop-color="#2f6df0"/>
        <stop offset="0.55" stop-color="#5ed6c0"/>
        <stop offset="1" stop-color="#c9d7ee"/>
      </linearGradient>
      <linearGradient id="portraitTone" x1="0" y1="0" x2="0" y2="1">
        <stop offset="0" stop-color="#c9ccd0"/>
        <stop offset="0.55" stop-color="#8a6a55"/>
        <stop offset="1" stop-color="#9a4a3c"/>
      </linearGradient>
      <linearGradient id="silverRing" x1="0" y1="0" x2="1" y2="1">
        <stop offset="0" stop-color="#ffffff"/>
        <stop offset="0.5" stop-color="#6f747c"/>
        <stop offset="1" stop-color="#e4e7ea"/>
      </linearGradient>
    </defs>
    <g role="img" aria-label="Blurred evening street scene with a glowing sparkler">
      <rect width="766" height="437" fill="url(#frontNight)"/>
      <rect width="766" height="437" fill="url(#frontGlow)"/>
    </g>
    <circle cx="194" cy="211" r="220" fill="none" stroke="url(#ringMagenta)" stroke-width="4"/>
    <circle cx="205" cy="220" r="192" fill="none" stroke="url(#ringMagenta)" stroke-width="4"/>
    <circle cx="196" cy="221" r="311" fill="none" stroke="url(#arcViolet)" stroke-width="4"/>
    <circle cx="262" cy="221" r="504" fill="none" stroke="url(#arcSky)" stroke-width="5"/>
    <circle cx="181" cy="219" r="116" fill="url(#portraitTone)" role="img" aria-label="Portrait of the photographer on a city street"/>
    <circle cx="181" cy="219" r="116" fill="none" stroke="url(#silverRing)" stroke-width="5"/>
    <circle cx="181" cy="219" r="106" fill="none" stroke="#111" stroke-width="4"/>
  </svg>

  <div class="identity">
    <h1 class="identity__name">TAVO M.</h1>
    <p class="identity__role">Travel Photographer</p>
    <p class="identity__note">self-proclaimed</p>
  </div>
  <p class="identity__site">wanderingtavo.example</p>
  <div class="social">
    <span class="social__mark"></span>
    <p class="social__handles">@wandering_with_tavo<br>@wandering_with_tavo_2.0</p>
  </div>
</section>

<section class="card card--back">
  <svg class="card__art" viewBox="0 0 766 437" xmlns="http://www.w3.org/2000/svg">
    <defs>
      <linearGradient id="backDusk" x1="0" y1="0" x2="0" y2="1">
        <stop offset="0" stop-color="#2e3748"/>
        <stop offset="0.5" stop-color="#3d3b47"/>
        <stop offset="1" stop-color="#1a1d26"/>
      </linearGradient>
      <radialGradient id="backGlow" cx="0.3" cy="0.55" r="0.35">
        <stop offset="0" stop-color="#c7683a" stop-opacity="0.75"/>
        <stop offset="1" stop-color="#c7683a" stop-opacity="0"/>
      </radialGradient>
      <radialGradient id="backSpark" cx="0.5" cy="0.2" r="0.25">
        <stop offset="0" stop-color="#f1b27a" stop-opacity="0.5"/>
        <stop offset="1" stop-color="#f1b27a" stop-opacity="0"/>
      </radialGradient>
      <linearGradient id="portraitToneBack" x1="0" y1="0" x2="0" y2="1">
        <stop offset="0" stop-color="#c9ccd0"/>
        <stop offset="0.55" stop-color="#8a6a55"/>
        <stop offset="1" stop-color="#9a4a3c"/>
      </linearGradient>
      <linearGradient id="silverRingBack" x1="0" y1="0" x2="1" y2="1">
        <stop offset="0" stop-color="#ffffff"/>
        <stop offset="0.5" stop-color="#6f747c"/>
        <stop offset="1" stop-color="#e4e7ea"/>
      </linearGradient>
    </defs>
    <g role="img" aria-label="Blurred dusk sky with sunset glow and sparkler light">
      <rect width="766" height="437" fill="url(#backDusk)"/>
      <rect width="766" height="437" fill="url(#backGlow)"/>
      <rect width="766" height="437" fill="url(#backSpark)"/>
    </g>
    <ellipse cx="383" cy="230" rx="372" ry="330" fill="none" stroke="#0b0c10" stroke-width="7" opacity="0.85"/>
    <circle cx="381" cy="218" r="179" fill="none" stroke="#0b0c10" stroke-width="5"/>
    <circle cx="381" cy="226" r="114" fill="url(#portraitToneBack)" role="img" aria-label="Portrait of the photographer on a city street"/>
    <circle cx="381" cy="226" r="114" fill="none" stroke="url(#silverRingBack)" stroke-width="6"/>
  </svg>
  <p class="motto">OFFENDING PEOPLE SINCE 1986</p>
  <p class="postscript">ps. travelling made me fatter</p>
</section>

</body>
</html>
```